Powepoint Templates From Logo

We need 3 Powerpoint templates for use in a variety of presentations we develop and customize. Primary uses of the powerpoint presentations are for printed "pitch books" describing our firm's capabilities and approach (a lot of words with some design elements that we have developed), printed presentations of the results of financial evaluations of our clients (lots of charts and graphs) and as the talking points for speeches.

The design needs to be professional and "solid" to establish that we are capable of selling your multi-million dollar business, but also be a little different to show that we are not just boring MBA's.

Our current website and other materials have been developed internally and leave a great deal to be desired. I have initiated this project to demonstrate how much our look can be improved and, if successful, I hope to do much bigger projects in the future.
Updates

This is my first project and I thaank you all for your participation. Since I am new to this, I don;t know if I am providing the help and feedback as I should. Please feel free to let me know how I can be a better customer.

Target Market(s)

professionals (lawyers, accountaants), business owners, business groups, technology people

Industry/Entity Type

Financial

Requirements
Must have
• our logo
a place where logo of client can be inserted if appropriate
templates for the following pages
title page
standard bullet narrative page
page for charts and graphs to mostly fill the page
Should not have a lot of dark solid color that has to be printed.

Nice to have
• something to perk up the color a little

```html
<!DOCTYPE html>
<html lang="en">
<head>
<meta charset="utf-8">
<title>Halvorsen Advisory – Presentation Templates</title>
<link rel="stylesheet" href="https://fonts.googleapis.com/css2?family=Roboto+Condensed:wght@400;700&family=Arimo:wght@400;700&display=swap">
<style>
  :root {
    --navy: #1b2d5e;
    --navy-deep: #142349;
    --navy-band: #22376c;
    --navy-panel: #1f3366;
    --accent: #2c9fdc;
    --ink: #1a1a1a;
    --paper: #ffffff;
    --stage: #e8e8e6;
    --rule: #8a9cc2;
    --bar-blue: #8fa9d2;
    --bar-green: #5cb85a;
    --line-orange: #f0901e;
    --line-red: #b8262a;
  }
  * { box-sizing: border-box; margin: 0; padding: 0; }
  html, body { width: 1200px; height: 900px; overflow: hidden; }
  body { background: var(--stage); position: relative; font-family: "Arimo", Arial, sans-serif; color: var(--ink); }

  .slide { position: absolute; width: 548px; height: 410px; overflow: hidden; background: var(--paper); }
  .slide--title   { left: 38px;  top: 38px; }
  .slide--about   { left: 610px; top: 38px; }
  .slide--chart   { left: 38px;  top: 470px; }
  .slide--closing { left: 610px; top: 470px; }

  .slide--dark { background: linear-gradient(180deg, #25396e 0%, var(--navy) 45%, var(--navy-deep) 100%); color: var(--paper); }

  /* footer band */
  .footer { position: absolute; left: 0; right: 0; bottom: 0; height: 29px; background: var(--navy-band); color: var(--paper); display: flex; align-items: center; }
  .footer__url { font-family: "Arimo", Arial, sans-serif; font-size: 11px; letter-spacing: 1.6px; }
  .footer--right { justify-content: flex-end; padding-right: 14px; }
  .footer__brand { font-family: "Arimo", Arial, sans-serif; font-weight: 700; font-size: 12px; padding-left: 40px; width: 173px; height: 100%; display: flex; align-items: center; border-right: 1px solid rgba(255,255,255,.45); letter-spacing: .2px; }
  .footer__brand-url { padding-left: 10px; font-size: 9px; letter-spacing: 1.4px; }
  .footer__page { position: absolute; left: 379px; right: 0; top: 0; bottom: 0; display: flex; align-items: center; justify-content: center; font-family: "Roboto Condensed", Arial, sans-serif; font-weight: 700; font-size: 19px; letter-spacing: 4px; }

  /* wordmark */
  .wordmark { position: absolute; display: flex; align-items: center; gap: 8px; font-family: "Roboto Condensed", Arial, sans-serif; font-weight: 700; color: var(--paper); font-size: 19px; letter-spacing: .3px; }
  .wordmark__square { width: 22px; height: 22px; border: 2px solid var(--paper); }

  /* title slide */
  .slide--title .wordmark { left: 36px; top: 188px; }
  .title-block { position: absolute; left: 271px; top: 146px; }
  .title-block__heading { font-family: "Roboto Condensed", Arial, sans-serif; font-weight: 700; font-size: 36px; line-height: 39px; text-transform: uppercase; }
  .title-block__sub { margin-top: 10px; font-family: "Arimo", Arial, sans-serif; font-size: 14.5px; color: var(--accent); letter-spacing: .3px; }

  /* section heading */
  .section-head { position: absolute; left: 0; top: 34px; display: flex; align-items: center; }
  .section-head__num { width: 58px; height: 30px; background: var(--navy); color: var(--paper); font-family: "Roboto Condensed", Arial, sans-serif; font-weight: 700; font-size: 30px; display: flex; align-items: center; justify-content: flex-end; padding-right: 8px; }
  .section-head__title { margin-left: 14px; font-family: "Roboto Condensed", Arial, sans-serif; font-weight: 700; font-size: 29px; color: var(--navy); text-transform: uppercase; letter-spacing: .3px; }

  .body-copy { position: absolute; font-size: 12.4px; line-height: 14.8px; color: var(--ink); }
  .slide--about .body-copy { left: 72px; top: 77px; width: 214px; }
  .slide--chart .body-copy { left: 394px; top: 100px; width: 142px; text-align: justify; font-size: 11.2px; line-height: 13.6px; }

  /* side panel with fade */
  .side-panel { position: absolute; top: 0; bottom: 29px; left: 379px; right: 0; background: var(--paper); }
  .side-fade { position: absolute; top: 0; bottom: 29px; left: 320px; width: 59px; background: linear-gradient(90deg, rgba(0,0,0,0) 0%, rgba(0,0,0,.07) 70%, rgba(0,0,0,.12) 100%); }

  .contents { padding: 30px 0 0 15px; }
  .contents__title { font-family: "Roboto Condensed", Arial, sans-serif; font-weight: 700; font-size: 31px; color: var(--navy); text-transform: uppercase; margin-bottom: 13px; }
  .contents__list { list-style: none; }
  .contents__item { display: flex; align-items: flex-end; height: 37px; width: 131px; border-bottom: 1px solid var(--rule); padding-bottom: 1px; }
  .contents__item:first-child { height: 24px; }
  .contents__num { width: 22px; height: 17px; background: var(--navy); color: var(--paper); font-family: "Roboto Condensed", Arial, sans-serif; font-weight: 700; font-size: 15px; display: flex; align-items: center; justify-content: center; margin-right: 10px; }
  .contents__label { font-family: "Arimo", Arial, sans-serif; font-weight: 700; font-size: 12.5px; color: var(--navy); line-height: 17px; }

  /* chart */
  .chart { position: absolute; left: 34px; top: 92px; width: 270px; height: 240px; }
  .chart text { font-family: "Arimo", Arial, sans-serif; }

  /* closing */
  .closing-panel { position: absolute; top: 0; bottom: 29px; left: 379px; right: 0; background: var(--navy-panel); }
  .slide--closing .wordmark { left: 98px; top: 206px; }
  .closing__thanks { position: absolute; left: 379px; right: 0; top: 203px; text-align: center; font-family: "Roboto Condensed", Arial, sans-serif; font-weight: 700; font-size: 26px; color: var(--accent); text-transform: uppercase; }
  .slide--closing .footer { background: var(--navy-deep); }
</style>
</head>
<body>

<!-- Title slide -->
<section class="slide slide--dark slide--title">
  <div class="wordmark"><span class="wordmark__square"></span>HALVORSEN ADVISORY</div>
  <div class="title-block">
    <h1 class="title-block__heading">Lorem Ipsum<br>Dolor Sit Amet</h1>
    <p class="title-block__sub">Lorem Ipsum Dolor sit Amet</p>
  </div>
  <footer class="footer footer--right"><span class="footer__url">www.halvorsenadvisory.com</span></footer>
</section>

<!-- Narrative slide -->
<section class="slide slide--about">
  <div class="section-head"><span class="section-head__num">1</span><h2 class="section-head__title">About Us</h2></div>
  <p class="body-copy">Lorem ipsum dolor sit amet, consectetur adipisicing elit, sed do eiusmod tempor incididunt ut labore et dolore magna aliqua. Ut enim ad minim veniam, quis nostrud exercitation ullamco laboris nisi ut aliquip ex ea commodo consequat. Duis aute irure dolor in reprehenderit in voluptate velit esse cillum dolore eu fugiat nulla pariatur. Excepteur sint occaecat cupidatat non proident, sunt in culpa qui officia deserunt mollit anim id est laborum</p>
  <div class="side-fade"></div>
  <aside class="side-panel">
    <nav class="contents">
      <h3 class="contents__title">Project</h3>
      <ol class="contents__list">
        <li class="contents__item"><span class="contents__num">1</span><span class="contents__label">About us</span></li>
        <li class="contents__item"><span class="contents__num">2</span><span class="contents__label">Graphic</span></li>
        <li class="contents__item"><span class="contents__num">3</span><span class="contents__label">About us</span></li>
        <li class="contents__item"><span class="contents__num">4</span><span class="contents__label">About us</span></li>
        <li class="contents__item"><span class="contents__num">5</span><span class="contents__label">About us</span></li>
      </ol>
    </nav>
  </aside>
  <footer class="footer">
    <span class="footer__brand">HALVORSEN ADVISORY</span>
    <span class="footer__url footer__brand-url">www.halvorsenadvisory.com</span>
    <span class="footer__page">&lt; 1 &gt;</span>
  </footer>
</section>

<!-- Chart slide -->
<section class="slide slide--chart">
  <div class="section-head"><span class="section-head__num">2</span><h2 class="section-head__title">Graphic</h2></div>
  <svg class="chart" viewBox="0 0 270 240" role="img" aria-label="Bar and line chart of sales employees, bonus versus sales year to date">
    <text x="140" y="8" font-size="6.5" font-weight="700" text-anchor="middle" fill="#222">Sales Employees - Bonus vs. SalesYTD</text>
    <g stroke="#c8c8c8" stroke-width=".6">
      <line x1="30" y1="15" x2="253" y2="15"/><line x1="30" y1="44" x2="253" y2="44"/>
      <line x1="30" y1="73" x2="253" y2="73"/><line x1="30" y1="102" x2="253" y2="102"/>
      <line x1="30" y1="131" x2="253" y2="131"/><line x1="30" y1="160" x2="253" y2="160" stroke="#888"/>
    </g>
    <g font-size="4.5" fill="#444" text-anchor="end">
      <text x="27" y="17">100 %</text><text x="27" y="46">80 %</text><text x="27" y="75">60 %</text>
      <text x="27" y="104">40 %</text><text x="27" y="133">20 %</text><text x="27" y="162">0 %</text>
    </g>
    <g fill="var(--bar-blue)">
      <rect x="33" y="51" width="5" height="109"/><rect x="46" y="70" width="5" height="90"/>
      <rect x="59" y="76" width="5" height="84"/><rect x="72" y="80" width="5" height="80"/>
      <rect x="85" y="85" width="5" height="75"/><rect x="98" y="92" width="5" height="68"/>
      <rect x="111" y="95" width="5" height="65"/><rect x="124" y="102" width="5" height="58"/>
      <rect x="137" y="105" width="5" height="55"/><rect x="150" y="105" width="5" height="55"/>
      <rect x="163" y="114" width="5" height="46"/><rect x="176" y="119" width="5" height="41"/>
      <rect x="189" y="128" width="5" height="32"/><rect x="202" y="131" width="5" height="29"/>
      <rect x="215" y="145" width="5" height="15"/><rect x="228" y="151" width="5" height="9"/>
      <rect x="241" y="154" width="5" height="6"/>
    </g>
    <g fill="var(--bar-green)">
      <rect x="38" y="102" width="5" height="58"/><rect x="51" y="109" width="5" height="51"/>
      <rect x="64" y="56" width="5" height="104"/><rect x="77" y="90" width="5" height="70"/>
      <rect x="90" y="95" width="5" height="65"/><rect x="103" y="95" width="5" height="65"/>
      <rect x="116" y="119" width="5" height="41"/><rect x="129" y="99" width="5" height="61"/>
      <rect x="142" y="88" width="5" height="72"/><rect x="155" y="85" width="5" height="75"/>
      <rect x="168" y="80" width="5" height="80"/><rect x="181" y="76" width="5" height="84"/>
      <rect x="194" y="51" width="5" height="109"/><rect x="207" y="76" width="5" height="84"/>
      <rect x="220" y="122" width="5" height="38"/><rect x="233" y="114" width="5" height="46"/>
      <rect x="246" y="114" width="5" height="46"/>
    </g>
    <polyline fill="none" stroke="var(--line-red)" stroke-width="1.4" stroke-dasharray="4 2"
      points="38,152.8 51,145.5 64,128 77,128 90,116.5 103,105 116,99 129,90.4 142,80.3 155,70 168,58.5 181,46.9 194,32.4 207,26.6 220,22.3 233,19.4 246,17.9"/>
    <polyline fill="none" stroke="var(--line-orange)" stroke-width="1.4"
      points="38,142.6 51,123.8 64,105 77,90.4 90,75.9 103,64.3 116,55.6 129,46.9 142,38.2 155,32.4 168,26.6 181,22.3 194,19.4 207,17.9 220,16.5 233,15 246,15"/>
    <g fill="var(--line-orange)">
      <circle cx="38" cy="142.6" r="1.2"/><circle cx="51" cy="123.8" r="1.2"/><circle cx="64" cy="105" r="1.2"/>
      <circle cx="77" cy="90.4" r="1.2"/><circle cx="90" cy="75.9" r="1.2"/><circle cx="103" cy="64.3" r="1.2"/>
      <circle cx="116" cy="55.6" r="1.2"/><circle cx="129" cy="46.9" r="1.2"/><circle cx="142" cy="38.2" r="1.2"/>
      <circle cx="155" cy="32.4" r="1.2"/><circle cx="168" cy="26.6" r="1.2"/><circle cx="181" cy="22.3" r="1.2"/>
      <circle cx="194" cy="19.4" r="1.2"/><circle cx="207" cy="17.9" r="1.2"/><circle cx="220" cy="16.5" r="1.2"/>
      <circle cx="233" cy="15" r="1.2"/><circle cx="246" cy="15" r="1.2"/>
    </g>
    <g font-size="4" fill="#333" text-anchor="middle">
      <text x="90" y="71">58 %</text><text x="116" y="51">72 %</text><text x="142" y="34">84 %</text>
      <text x="168" y="22">92 %</text><text x="194" y="15">97 %</text><text x="220" y="12">99 %</text><text x="250" y="12">100 %</text>
    </g>
    <g>
      <rect x="60" y="18" width="44" height="27" fill="#fff6bd" stroke="#b8b08a" stroke-width=".5"/>
      <rect x="63" y="21" width="5" height="3.5" fill="var(--bar-green)"/><text x="70" y="24.3" font-size="4" fill="#333">Bonus</text>
      <rect x="63" y="27" width="5" height="3.5" fill="var(--bar-blue)"/><text x="70" y="30.3" font-size="4" fill="#333">Sales</text>
      <line x1="63" y1="34.8" x2="68" y2="34.8" stroke="var(--line-orange)" stroke-width="1"/><text x="70" y="36.3" font-size="4" fill="#333">Bonus trend</text>
      <line x1="63" y1="40.8" x2="68" y2="40.8" stroke="var(--line-red)" stroke-width="1" stroke-dasharray="2 1"/><text x="70" y="42.3" font-size="4" fill="#333">Sales trend</text>
    </g>
    <g font-size="4.6" fill="#333" text-anchor="end">
      <text transform="translate(40,165) rotate(-90)">Anders</text>
      <text transform="translate(53,165) rotate(-90)">Brandt</text>
      <text transform="translate(66,165) rotate(-90)">Carver</text>
      <text transform="translate(79,165) rotate(-90)">Dalton</text>
      <text transform="translate(92,165) rotate(-90)">Ellison</text>
      <text transform="translate(105,165) rotate(-90)">Fairbanks</text>
      <text transform="translate(118,165) rotate(-90)">Garner</text>
      <text transform="translate(131,165) rotate(-90)">Hollis</text>
      <text transform="translate(144,165) rotate(-90)">Ingram</text>
      <text transform="translate(157,165) rotate(-90)">Jarvis</text>
      <text transform="translate(170,165) rotate(-90)">Keller</text>
      <text transform="translate(183,165) rotate(-90)">Lomax</text>
      <text transform="translate(196,165) rotate(-90)">Mercer</text>
      <text transform="translate(209,165) rotate(-90)">Norris</text>
      <text transform="translate(222,165) rotate(-90)">Osborne</text>
      <text transform="translate(235,165) rotate(-90)">Prescott</text>
      <text transform="translate(248,165) rotate(-90)">Quinlan</text>
    </g>
  </svg>
  <div class="side-fade"></div>
  <aside class="side-panel"></aside>
  <p class="body-copy">Lorem ipsum dolor sit amet, consectetur adipisicing elit, sed do eiusmod tempor incididunt ut labore et dolore magna aliqua. Ut enim ad minim veniam, quis nostrud exercitation ullamco laboris nisi ut aliquip ex ea commodo consequat. Duis aute irure dolor in reprehenderit in voluptate velit esse cillum dolore eu fugiat nulla pariatur. Excepteur sint occaecat cupidatat non proident, sunt in culpa qui officia deserunt mollit anim id est laborum</p>
  <footer class="footer">
    <span class="footer__brand">HALVORSEN ADVISORY</span>
    <span class="footer__url footer__brand-url">www.halvorsenadvisory.com</span>
    <span class="footer__page">&lt; 2 &gt;</span>
  </footer>
</section>

<!-- Closing slide -->
<section class="slide slide--dark slide--closing">
  <div class="closing-panel"></div>
  <div class="wordmark"><span class="wordmark__square"></span>HALVORSEN ADVISORY</div>
  <p class="closing__thanks">Thank You</p>
  <footer class="footer footer--right"><span class="footer__url">www.halvorsenadvisory.com</span></footer>
</section>

</body>
</html>
```